Bluestone Advisory & Mgmt - Professional Business Cards

Hi!

I am a Real Estate Developer and Construction Consultant.

I have a lot of inspiration from previous designs and would be open to using the attached Designs as a starting point. I would like to see these styles incorporated into your designs.

I really need professional business card to go with it that includes my important info.

Look forward to seeing your designs!.

Target Market(s)

My Target market are building owners, lawyers, consultants.

Industry/Entity Type

Real Estate Development

Contact Information for Business Card

My Name: Dorian Pelkey
My Title: Principle
Company Name: Bluestone Advisory & Mgmt, LLC
Address: 348 West 71st Street, 9th FL New York, NY 10010
Mobile: 917.806.3971
Website: bam-hvx.example

Font styles to use
Serif
Sans Serif

Colors

Designer to choose colors to be used in the design.

Requirements
Must have
• Must incorporate the logo attached or have new that looks similar.
• Must use professional font that will be seen and judged by wealthy land owners and developers.
• Must incorporate some of the color green.
Should not have
• Photo's or pictures of people or buildings of any kind.

```html
<!DOCTYPE html>
<html lang="en">
<head>
<meta charset="utf-8">
<title>Bluestone Advisory &amp; Mgmt - Business Cards</title>
<link rel="stylesheet" href="https://fonts.googleapis.com/css2?family=Montserrat:wght@400;600&family=Open+Sans:wght@400;600&display=swap">
<style>
  :root {
    --backdrop: #2a2521;
    --paper: #ece9dc;
    --charcoal: #2f2d2c;
    --green: #3aa865;
    --green-light: #6cc291;
    --green-deep: #2f9a57;
    --ink: #1c1c1c;
    --white: #ffffff;
    --muted-grey: #9a9a96;
  }
  * { margin: 0; padding: 0; box-sizing: border-box; }
  html, body { width: 1200px; height: 787px; overflow: hidden; }
  body {
    background: var(--backdrop);
    font-family: "Open Sans", Arial, sans-serif;
    position: relative;
  }
  .card {
    position: absolute;
    top: 239px;
    width: 540px;
    height: 309px;
    box-shadow: 0 10px 28px rgba(0,0,0,.45);
    overflow: hidden;
  }
  .card--front { left: 50px; background: var(--paper); }
  .card--back { left: 610px; background: var(--charcoal); }

  /* front */
  .name-band {
    position: absolute;
    left: 110px; top: 12px; right: 12px; height: 176px;
    background: linear-gradient(100deg, var(--green-deep), var(--green-light));
  }
  .brand {
    position: absolute;
    display: flex; align-items: center; gap: 8px;
  }
  .brand__dot {
    width: 12px; height: 12px; border-radius: 50%;
  }
  .brand__name {
    font-family: "Montserrat", Arial, sans-serif;
    font-weight: 600;
    letter-spacing: 3px;
  }
  .brand__tagline {
    font-family: "Montserrat", Arial, sans-serif;
    font-weight: 400;
    letter-spacing: .5px;
  }
  .name-band .brand { left: 24px; top: 22px; }
  .name-band .brand__dot { background: var(--white); }
  .name-band .brand__name { color: var(--white); font-size: 22px; }
  .name-band .brand__tagline-line {
    position: absolute; left: 44px; top: 54px;
    color: var(--white); font-size: 9px;
  }
  .holder {
    position: absolute; right: 24px; bottom: 18px;
    text-align: right; color: var(--white);
  }
  .holder__name { font-size: 18px; font-weight: 400; }
  .holder__title { font-size: 9px; opacity: .85; }

  .address {
    position: absolute; left: 28px; top: 204px;
    font-size: 10.5px; line-height: 1.5; color: var(--ink);
  }
  .address__company { font-weight: 600; }
  .contact {
    position: absolute; left: 300px; top: 216px;
    list-style: none; font-size: 11px; font-weight: 600; color: var(--ink);
  }
  .contact li { display: flex; align-items: center; gap: 10px; margin-bottom: 8px; }
  .contact svg { width: 13px; height: 13px; fill: var(--ink); }
  .base-stripe {
    position: absolute; left: 12px; bottom: 14px; width: 340px; height: 10px;
    background: var(--green);
  }

  /* back */
  .card--back .brand {
    left: 0; right: 0; top: 96px; justify-content: center;
  }
  .card--back .brand__dot { background: var(--green-light); }
  .card--back .brand__name { color: var(--green-light); font-size: 30px; }
  .back-tagline {
    position: absolute; left: 0; right: 0; top: 140px; text-align: center;
    color: var(--muted-grey); font-family: "Montserrat", Arial, sans-serif; font-size: 10px; letter-spacing: 1px;
  }
  .web-strip {
    position: absolute; left: 12px; right: 12px; bottom: 16px; height: 38px;
    background: var(--paper);
    display: flex; align-items: center; gap: 10px; padding-left: 150px;
    font-size: 11px; color: var(--ink);
  }
  .web-strip svg { width: 14px; height: 14px; }
</style>
</head>
<body>

<section class="card card--front" aria-label="Business card front">
  <div class="name-band">
    <div class="brand">
      <span class="brand__dot"></span>
      <span class="brand__name">Bluestone</span>
    </div>
    <div class="brand__tagline brand__tagline-line">Advisory &amp; Mgmt, LLC</div>
    <div class="holder">
      <p class="holder__name">Dorian Pelkey</p>
      <p class="holder__title">Principle</p>
    </div>
  </div>

  <address class="address" style="font-style:normal">
    <p class="address__company">Bluestone Advisory &amp; Mgmt, LLC</p>
    <p>348 West 71st Street, 9th FL New York,</p>
    <p>NY 10010</p>
  </address>

  <ul class="contact">
    <li>
      <svg viewBox="0 0 24 24" aria-hidden="true"><path d="M6.6 10.8a15 15 0 0 0 6.6 6.6l2.2-2.2c.3-.3.7-.4 1-.2 1.1.4 2.3.6 3.6.6.6 0 1 .4 1 1V20c0 .6-.4 1-1 1A17 17 0 0 1 3 4c0-.6.4-1 1-1h3.5c.6 0 1 .4 1 1 0 1.3.2 2.5.6 3.6.1.3 0 .7-.2 1z"/></svg>
      <span>917.806.3971</span>
    </li>
    <li>
      <svg viewBox="0 0 24 24" aria-hidden="true"><path d="M2 5h20v14H2z M2 5l10 8 10-8" fill="none" stroke="#1c1c1c" stroke-width="2"/></svg>
      <span>info@bam-hvx.example</span>
    </li>
  </ul>

  <div class="base-stripe"></div>
</section>

<section class="card card--back" aria-label="Business card back">
  <div class="brand">
    <span class="brand__dot"></span>
    <span class="brand__name">Bluestone</span>
  </div>
  <p class="back-tagline">Advisory &amp; Mgmt, LLC</p>
  <div class="web-strip">
    <svg viewBox="0 0 24 24" aria-hidden="true" fill="none" stroke="#1c1c1c" stroke-width="1.6">
      <circle cx="12" cy="12" r="10"/>
      <ellipse cx="12" cy="12" rx="4.5" ry="10"/>
      <path d="M2 12h20M4 7h16M4 17h16"/>
    </svg>
    <span>www.bam-hvx.example</span>
  </div>
</section>

</body>
</html>
```